Company Website for an IT business called "BRIGHT CORRIDOR"

Complete website creation with text and graphics.
We need :
- modern and creative design for our IT company
- Content management system to edit text later on
- Integrate third party content from partner company
- Contact form (transfer by email)
Updates

Designs look the same

Target Market(s)

Small and medium business
private customers

Industry/Entity Type

Information Technology

Coding

Coded - Design and coding required

Number of Pages Required

1 page

Font styles to use
Sans Serif

Requirements
Must have
• Contact form
Link to legal information
Link to data protection (GDPR)
Link to website owner declaration
Nice to have
• Fresh and creative graphics for IT business

```html
<!DOCTYPE html>
<html lang="en">
<head>
<meta charset="utf-8">
<title>Bright Corridor – IT Services</title>
<link rel="stylesheet" href="https://fonts.googleapis.com/css2?family=Open+Sans:wght@400;600;700&display=swap">
<style>
:root{
  --blue:#1380d6;
  --blue-deep:#0f5fa6;
  --green:#6cbb16;
  --red:#f5002a;
  --ink:#1a1a1a;
  --text:#444;
  --white:#fff;
  --footer:#0e0e0e;
  --footer-text:#e6e6e6;
}
*{box-sizing:border-box;margin:0;padding:0}
html,body{width:1200px;height:3809px;overflow:hidden}
body{position:relative;font-family:"Open Sans",Arial,sans-serif;color:var(--ink);background:var(--white)}
a{color:inherit;text-decoration:none}
.abs{position:absolute}
.btn{position:absolute;display:flex;align-items:center;justify-content:center;border-radius:24px;background:var(--blue);color:var(--white);font-weight:600}

/* header */
.top-line{left:0;top:0;width:1200px;height:3px;background:linear-gradient(90deg,var(--green) 0 25%,#1b3d6b 25% 50%,var(--blue) 50% 75%,#f26522 75%)}
.site-header{left:0;top:3px;width:1200px;height:90px;background:var(--white)}
.brand{left:89px;top:44px;display:flex;align-items:center;gap:10px;font-size:24px;font-weight:700;color:#17406d;letter-spacing:1px}
.brand-dot{width:18px;height:18px;background:var(--blue)}
.nav{left:420px;top:36px;display:flex;gap:0;font-size:16px;font-weight:600}
.nav a{position:absolute;white-space:nowrap}
.nav .active{color:var(--blue)}
.quote{left:949px;top:22px;width:161px;height:47px;font-size:18px}

/* hero */
.hero{left:0;top:93px;width:1200px;height:541px;background:linear-gradient(120deg,#2c2522 0%,#5a4638 45%,#3d3029 70%,#7a6a5c 100%)}
.hero-title{left:90px;top:196px;font-size:66px;font-weight:700;color:var(--white)}
.hero-sub{left:90px;top:292px;width:480px;font-size:23px;line-height:30px;font-weight:700;color:var(--white)}
.hero-btn{left:90px;top:377px;width:160px;height:47px;font-size:18px}

/* about */
.about{left:0;top:634px;width:1200px;height:432px;background:linear-gradient(90deg,#0f4f8f 0%,#1471bf 40%,#1573c2 60%,#0f4f8f 100%);color:var(--white);text-align:center}
.about h2{position:absolute;left:0;width:1200px;top:95px;font-size:40px;font-weight:700}
.about p{position:absolute;left:155px;width:890px;top:158px;font-size:17px;line-height:29px}
.about-btn{left:514px;top:276px;width:170px;height:48px;background:var(--white);color:var(--blue);font-size:18px}

/* target audience */
.section-title{position:absolute;left:0;width:1200px;text-align:center;font-size:40px;font-weight:700;color:var(--ink)}
.card{position:absolute;top:1237px;width:325px;height:421px;background:var(--white);box-shadow:0 4px 18px rgba(0,0,0,.08)}
.card-photo{position:absolute;left:0;top:0;width:325px;height:225px}
.card-photo svg{position:absolute;left:0;bottom:0}
.card h3{position:absolute;left:19px;top:240px;font-size:25px;font-weight:400;color:var(--ink)}
.card p{position:absolute;left:19px;top:282px;width:295px;font-size:17px;line-height:27px;color:var(--text)}
.card .btn{left:19px;top:402px;width:127px;height:40px;font-size:17px;font-weight:400}

/* split sections */
.panel{position:absolute;width:600px;height:538px}
.panel h2{position:absolute;top:102px;font-size:40px;font-weight:700;color:var(--white)}
.panel ul{position:absolute;top:166px;width:440px;list-style:none;color:var(--white);font-size:15.5px;line-height:27px}
.panel li{position:relative;padding-left:24px;margin-bottom:16px}
.panel li::before{content:"";position:absolute;left:0;top:9px;width:7px;height:7px;border-radius:50%;background:var(--white)}
.panel .btn{top:390px;width:126px;height:42px;font-size:16px;font-weight:400}
.what{left:0;top:1788px;background:var(--green)}
.what h2,.what ul,.what .btn{left:91px}
.what ul li{color:var(--white)}
.what-photo{left:600px;top:1788px;background:linear-gradient(160deg,#7a5a44 0%,#b08462 45%,#5b4a3e 100%)}
.benefits-photo{left:0;top:2326px;background:linear-gradient(150deg,#c9ccd1 0%,#6f747c 40%,#2a2d33 70%,#d8cfc6 100%)}
.benefits{left:600px;top:2326px;background:var(--red)}
.benefits h2,.benefits ul,.benefits .btn{left:92px}

/* contact */
.touch p{position:absolute;left:155px;width:890px;top:3027px;text-align:center;font-size:17px;line-height:32px;color:var(--text)}
.touch-btn{left:514px;top:3114px;width:171px;height:48px;font-size:18px}

/* footer */
.site-footer{left:0;top:3271px;width:1200px;height:538px;background:var(--footer);color:var(--footer-text)}
.foot-col{position:absolute;top:80px}
.foot-col h4{font-size:18px;font-weight:600;color:var(--white);margin-bottom:22px}
.foot-col li{list-style:none;font-size:13.5px;line-height:31px}
.follow{position:absolute;left:992px;top:222px}
.follow h4{font-size:18px;font-weight:600;color:var(--white)}
.socials{display:flex;gap:17px;margin-top:20px}
.socials span{width:13px;height:13px;border-radius:50%;background:var(--white)}
.foot-rule{left:89px;top:335px;width:1022px;height:1px;background:#262626}
.news-title{left:180px;top:372px;font-size:26px;font-weight:700;color:var(--white)}
.news-input{left:529px;top:368px;width:442px;height:47px;background:#1b1b1b;font-size:15px;color:#bbb;display:flex;align-items:center;padding-left:17px}
.news-send{left:971px;top:368px;width:49px;height:47px;background:var(--blue);display:flex;align-items:center;justify-content:center}
.copyright{left:0;width:1200px;top:484px;text-align:center;font-size:12.5px;color:var(--white)}
</style>
</head>
<body>

<div class="abs top-line"></div>
<header class="abs site-header">
  <div class="abs brand" style="top:30px"><span class="brand-dot"></span>BRIGHT CORRIDOR</div>
  <nav class="abs nav" style="left:0;top:0">
    <a class="active" style="left:420px;top:33px">Home</a>
    <a style="left:507px;top:33px">Services</a>
    <a style="left:613px;top:33px">Resources</a>
    <a style="left:735px;top:33px">Blog</a>
    <a style="left:810px;top:33px">Contact Us</a>
  </nav>
  <a class="btn quote">Get a Quote</a>
</header>

<section class="abs hero" role="img" aria-label="Photo of a team meeting around a desk in a warm office"></section>
<h1 class="abs hero-title">Bright Corridor</h1>
<p class="abs hero-sub">Lorem ipsum dolor sit amet, consectetur elit, sed do eiusmod tempor incididunt</p>
<a class="btn hero-btn">Get Started</a>

<section class="abs about" role="region" aria-label="About us">
  <h2>ABOUT US</h2>
  <p>Lorem ipsum dolor sit amet, consectetur adipiscing elit, sed do eiusmod tempor incididunt ut labore et dolore magna aliqua. Ut enim ad minim veniam, quis nostrud exercitation ullamco laboris nisi ut aliquip ex ea commodo consequat. Duis aute irure dolor in reprehenderit in voluptate velit esse cillum dolore eu fugiat nulla pariatur.</p>
  <a class="btn about-btn">Read More</a>
</section>

<h2 class="section-title" style="top:1160px">TARGET AUDIENCE</h2>

<article class="card" style="left:90px">
  <div class="card-photo" role="img" aria-label="Photo of a business owner shaking hands" style="background:linear-gradient(135deg,#9aa3ad,#3e4a5c 60%,#c5a58a)">
    <svg width="325" height="32" viewBox="0 0 325 32"><polygon points="0,32 162.5,0 325,32" fill="#fff"/></svg>
  </div>
  <h3>Lorem ipsum dolor</h3>
  <p>Lorem ipsum dolor sit amet, tetur adipiscing elit, sed do eiusmod tempor incididunt ut labore et dolore magna aliqua.</p>
  <a class="btn">Read More</a>
</article>
<article class="card" style="left:437px">
  <div class="card-photo" role="img" aria-label="Photo of a private customer in a workshop" style="background:linear-gradient(135deg,#1f2a3a,#3c5676 55%,#8ea3b8)">
    <svg width="325" height="32" viewBox="0 0 325 32"><polygon points="0,32 162.5,0 325,32" fill="#fff"/></svg>
  </div>
  <h3>Lorem ipsum dolor</h3>
  <p>Lorem ipsum dolor sit amet, tetur adipiscing elit, sed do eiusmod tempor incididunt ut labore et dolore magna aliqua.</p>
  <a class="btn">Read More</a>
</article>
<article class="card" style="left:785px">
  <div class="card-photo" role="img" aria-label="Photo of a small team working at laptops" style="background:linear-gradient(135deg,#d9d4cc,#8a7d70 50%,#2d2a28)">
    <svg width="325" height="32" viewBox="0 0 325 32"><polygon points="0,32 162.5,0 325,32" fill="#fff"/></svg>
  </div>
  <h3>Lorem ipsum dolor</h3>
  <p>Lorem ipsum dolor sit amet, tetur adipiscing elit, sed do eiusmod tempor incididunt ut labore et dolore magna aliqua.</p>
  <a class="btn">Read More</a>
</article>

<section class="panel what">
  <h2>WHAT WE DO</h2>
  <ul>
    <li>Lorem ipsum dolor sit amet, consectetur adipiscing elit, sed do eiusmod tempor incididunt ut labore et</li>
    <li>Lorem ipsum dolor sit amet, consectetur adipiscing elit, sed do eiusmod tempor incididunt ut labore et</li>
    <li>Lorem ipsum dolor sit amet, consectetur adipiscing elit, sed do eiusmod tempor incididunt ut labore et</li>
  </ul>
  <a class="btn">Read More</a>
</section>
<div class="panel what-photo" role="img" aria-label="Photo of a smiling professional at a laptop in an open office"></div>

<div class="panel benefits-photo" role="img" aria-label="Photo of hands on a laptop showing an analytics dashboard"></div>
<section class="panel benefits">
  <h2>BENEFITS</h2>
  <ul>
    <li>Lorem ipsum dolor sit amet, consectetur adipiscing elit, sed do eiusmod tempor incididunt ut labore et</li>
    <li>Lorem ipsum dolor sit amet, consectetur adipiscing elit, sed do eiusmod tempor incididunt ut labore et</li>
    <li>Lorem ipsum dolor sit amet, consectetur adipiscing elit, sed do eiusmod tempor incididunt ut labore et</li>
  </ul>
  <a class="btn">Read More</a>
</section>

<section class="touch">
  <h2 class="section-title" style="top:2956px">GET IN TOUCH</h2>
  <p>Lorem ipsum dolor sit amet, consectetur adipiscing elit, sed do eiusmod tempor incididunt ut laboraliqua. Ut enim ad minim veniam, quis nostrud exercitation ullamco laboris nisi ut aliquip ex ea commodo consequat.</p>
  <a class="btn touch-btn">Contact Us</a>
</section>

<footer class="abs site-footer">
  <div class="foot-col" style="left:89px">
    <h4>Company</h4>
    <ul><li>Home</li><li>Services</li><li>Resources</li><li>Blog</li><li>Contact Us</li></ul>
  </div>
  <div class="foot-col" style="left:369px">
    <h4>Contact Us</h4>
    <ul><li>hello@brightcorridor.com</li><li>+8 555 010 010</li><li>24, Lantern Lane L - 5120</li><li>Westbrook</li></ul>
  </div>
  <div class="foot-col" style="left:693px">
    <h4>Legal</h4>
    <ul><li>Legal information</li><li>Data protection (GDPR)</li><li>Website owner declaration</li></ul>
  </div>
  <div class="foot-col" style="left:992px">
    <h4>My Account</h4>
    <ul><li>Log in</li><li>Sign Up</li></ul>
  </div>
  <div class="follow">
    <h4>Follow Us</h4>
    <div class="socials" aria-label="Social links"><span></span><span></span><span></span><span></span></div>
  </div>
  <div class="abs foot-rule"></div>
  <div class="abs news-title">Sign up Our Newsletter</div>
  <div class="abs news-input">Email Address</div>
  <div class="abs news-send" aria-label="Send">
    <svg width="22" height="22" viewBox="0 0 24 24" fill="none" stroke="#fff" stroke-width="2" stroke-linejoin="round"><path d="M22 2 2 10l8 3 3 8z"/><path d="M22 2 10 13"/></svg>
  </div>
  <p class="abs copyright">© 2021 The Company name. All rights Reserved.Privacy Policy | Terms Of Use</p>
</footer>

</body>
</html>
```